Business Card Design

Provide project management services to the construction and other industries
Construction services - Civil and Concrete works
Shop Detailing
Structural Modelling
Client side coordination of project teams and consultants
Feasibility Studies for construction projects

Industry/Entity Type

Business

Contact Information for Business Card

Crestline Ops
Darrel Pikett B.Sc (Civil), M.Proj.Mgt.
Principal

m: 0412 583 716
e: dpikett@crestlineops.com.au

p: 08 6293 4078
a: 17 Bramblewood Court, Marrowvale, WA 6058

```html
<!DOCTYPE html>
<html lang="en">
<head>
<meta charset="utf-8">
<title>Crestline Ops – Business Card</title>
<link href="https://fonts.googleapis.com/css2?family=Arimo:wght@400;700&family=Open+Sans:wght@400;700&display=swap" rel="stylesheet">
<style>
  :root {
    --backdrop: #e9e6e1;
    --card: #ffffff;
    --card-edge: #3a3a3a;
    --ink: #1a1a1a;
    --muted: #444444;
    --divider: #8a8a8a;
    --accent: #1e8a1e;
  }
  * { margin: 0; padding: 0; box-sizing: border-box; }
  html, body {
    width: 1200px; height: 1000px; overflow: hidden;
    background: var(--backdrop);
  }
  .canvas { position: relative; width: 1200px; height: 1000px; }
  .card {
    position: absolute; left: 294px; width: 610px; height: 358px;
    background: var(--card);
    border: 1px solid var(--card-edge);
    box-shadow: 0 4px 10px rgba(0,0,0,0.18);
  }
  .card--front { top: 127px; }
  .card--back { top: 515px; height: 357px; }

  .wordmark {
    position: absolute; left: 0; right: 0; text-align: center;
    font-family: "Arimo", Arial, sans-serif; font-weight: 700;
    font-size: 44px; letter-spacing: 1px; color: var(--ink);
    text-transform: uppercase; line-height: 1;
  }
  .card--front .wordmark { top: 136px; }
  .card--back .wordmark { top: 93px; }

  .services {
    position: absolute; left: 23px; right: 24px; top: 261px;
    font-family: "Arimo", Arial, sans-serif; font-size: 18px;
    color: var(--ink); line-height: 23px;
  }
  .services__line {
    display: flex; justify-content: space-between; white-space: nowrap;
  }
  .services__line--tight { justify-content: flex-start; gap: 10px; }
  .services__line--tight > span:last-child { margin-left: auto; }
  .sep { color: var(--divider); font-size: 15px; }
  .sep--accent { color: var(--accent); }

  .contact {
    position: absolute; left: 0; right: 0; text-align: center;
    font-family: "Open Sans", Arial, sans-serif; color: var(--ink);
  }
  .contact__name { top: 195px; font-size: 18px; font-weight: 700; }
  .contact__role { top: 220px; font-size: 15px; line-height: 23px; }
  .contact__address { top: 297px; font-size: 14px; color: var(--muted); }
  .contact__lines { top: 323px; font-size: 14px; color: var(--muted); }
  .contact__lines .sep { font-size: 14px; margin: 0 5px; }
</style>
</head>
<body>
<div class="canvas">
  <section class="card card--front">
    <div class="wordmark">Crestline Ops</div>
    <div class="services">
      <div class="services__line"><span>Project</span><span>Management</span><span>Services</span><span class="sep">|</span><span>Civil</span><span>and</span><span>Concrete</span><span>Works</span></div>
      <div class="services__line"><span>Construction Services</span><span class="sep">|</span><span>Shop Detailing</span><span class="sep sep--accent">|</span><span>Client Side Coordination</span></div>
      <div class="services__line"><span>Structural Modelling</span><span class="sep sep--accent">|</span><span>Feasibility Studies For Construction Projects</span></div>
    </div>
  </section>

  <section class="card card--back">
    <div class="wordmark">Crestline Ops</div>
    <div class="contact contact__name">Darrel Pikett</div>
    <div class="contact contact__role">B.Sc (Civil), M.Proj.Mgt.<br>Principal</div>
    <div class="contact contact__address">17 Bramblewood Court, Marrowvale, WA 6058</div>
    <div class="contact contact__lines">M: 0412 583 716<span class="sep">|</span>P: 08 6293 4078<span class="sep sep--accent">|</span>E: dpikett@crestlineops.com.au</div>
  </section>
</div>
</body>
</html>
```